Professional Business Card - TWO SIDES

I need a new business card design to be used by myself and my employees. I would like a professional card and for the front I thought I would like a dark blue thatch with our logo in a raised gold foil on top of it. On the other side I would like name, position, and contact info. I've uploaded our old design for an example of the info used.

Target Market(s)

Business Clients

Industry/Entity Type

CPA Firm

Contact Information for Business Card

Logo, Name, Title, Address, Phone Numbers, Website address, Email Address

Font styles to use
Serif
Sans Serif

Colors
0054AA
0677BA
7BADD7
CADEEF
E8F1F8
0094D4
00A9DD
6FCCEA
C7EBF8
E9F6FB

Requirements
Must have
• Modern Professional Look
Nice to have
• Logo in Gold Foil or ability to have is raised. I like our logo in a single color
Should not have
• I've uploaded old business card

```html
<!DOCTYPE html>
<html lang="en">
<head>
<meta charset="utf-8">
<title>Halden &amp; Halden – Business Card</title>
<link rel="stylesheet" href="https://fonts.googleapis.com/css2?family=Arimo:wght@400;700&display=swap">
<style>
  :root {
    --backdrop: #e8f1f8;
    --navy: #0a2a52;
    --navy-deep: #07203f;
    --thatch-a: rgba(0, 84, 170, 0.22);
    --thatch-b: rgba(6, 119, 186, 0.16);
    --edge: #0094d4;
    --gold: #d4b25a;
    --name: #6fccea;
    --text-light: #e9f6fb;
    --rule: #7badd7;
  }
  * { box-sizing: border-box; margin: 0; padding: 0; }
  html, body {
    width: 1200px; height: 801px; overflow: hidden;
    background: var(--backdrop);
    font-family: "Arimo", Arial, sans-serif;
  }
  .canvas {
    position: relative; width: 1200px; height: 801px;
    display: flex; align-items: center; justify-content: center; gap: 60px;
  }
  .card {
    position: relative; width: 525px; height: 300px;
    background-color: var(--navy);
    background-image:
      repeating-linear-gradient(45deg, var(--thatch-a) 0 1px, transparent 1px 6px),
      repeating-linear-gradient(-45deg, var(--thatch-b) 0 1px, transparent 1px 6px);
    border-bottom: 4px solid var(--edge);
    border-left: 2px solid var(--edge);
    box-shadow: 0 10px 24px rgba(7, 32, 63, 0.25);
  }
  .card--info { display: flex; align-items: center; }
  .brand {
    width: 52%; padding-left: 32px;
    font-weight: 700; font-size: 21px; letter-spacing: 1px;
    color: var(--gold); text-transform: uppercase; white-space: nowrap;
  }
  .divider { width: 1px; height: 190px; background: var(--rule); }
  .details { padding-left: 26px; color: var(--text-light); }
  .details__name {
    color: var(--name); font-weight: 700; font-size: 24px; line-height: 1.1;
    white-space: nowrap;
  }
  .details__role { font-size: 15px; margin-bottom: 18px; }
  .details__address { font-size: 15px; line-height: 1.35; margin-bottom: 18px; }
  .contact { list-style: none; font-size: 15px; line-height: 1.5; }
  .contact li { display: flex; align-items: center; gap: 9px; white-space: nowrap; }
  .contact svg { width: 14px; height: 14px; flex: none; }
  .card--mark {
    display: flex; align-items: center; justify-content: center;
    background-color: var(--navy-deep);
  }
  .brand--foil {
    width: auto; padding: 0;
    font-size: 38px; letter-spacing: 2px;
  }
</style>
</head>
<body>
<main class="canvas">
  <section class="card card--info" aria-label="Card side with contact details">
    <div class="brand">Halden &amp; Halden</div>
    <div class="divider"></div>
    <div class="details">
      <p class="details__name">Daniel Carter</p>
      <p class="details__role">Manager</p>
      <p class="details__address">Your address, city<br>state, ZIP 0000</p>
      <ul class="contact">
        <li>
          <svg viewBox="0 0 14 14" aria-hidden="true"><path d="M3 1 L5 4 L4 5.5 Q5.5 8.5 8.5 10 L10 9 L13 11 L11.5 13 Q5 12.5 1 3 Z" fill="var(--name)"/></svg>
          123-456-2100
        </li>
        <li>
          <svg viewBox="0 0 14 14" aria-hidden="true"><rect x="1" y="3" width="12" height="8.5" fill="none" stroke="var(--name)" stroke-width="1.5"/><path d="M1 3 L7 8 L13 3" fill="none" stroke="var(--name)" stroke-width="1.5"/></svg>
          youremail@mailbox.com
        </li>
        <li>
          <svg viewBox="0 0 14 14" aria-hidden="true"><circle cx="7" cy="7" r="6" fill="var(--name)"/><path d="M1 7 H13 M7 1 V13 M2.5 4 H11.5 M2.5 10 H11.5" stroke="var(--navy)" stroke-width="0.8"/></svg>
          www.yourwebsite.com
        </li>
      </ul>
    </div>
  </section>

  <section class="card card--mark" aria-label="Card side with gold foil firm name">
    <div class="brand brand--foil">Halden &amp; Halden</div>
  </section>
</main>
</body>
</html>
```